IT Company Business Card Rebranding

We want to modernize our business cards massively. We want to incorporate aspects of our old business card such as the white and geometric design with the blues of another icon. Existing Logo, old business card and icon are all attached.

We are a modern IT company that provides support for new and growing technologies and want our business cards to be modern yet professional.
Updates

Note: Do not use file ICON.png in design. This is just a design we like Added Wednesday, March 9, 2016

Industry/Entity Type

Information Technology

Contact Information for Business Card

Roughly 43 : 26 or 1075 x 650 px

Font styles to use
Serif

Colors
0492cd
3276b5
33a6d7
86cfc6
cfeae6
cee9f5
ffffff

Requirements
Must have
• Modern yet professional
Nice to have
• We would like to incorporate the blues of our existing logo and of the icon provided. Really like the design of the icon.
Should not have
• Too Decorative. Just simple and professional.
• Not have the circle icon, as it is a copyrighted icon, I just like the colors and the geometric design

```html
<!DOCTYPE html>
<html lang="en">
<head>
<meta charset="utf-8">
<title>Nimbra Tech – Business Card</title>
<link rel="stylesheet" href="https://fonts.googleapis.com/css2?family=Questrial&display=swap">
<style>
  :root{
    --bg:#1c1c1c;
    --card:#ffffff;
    --ink:#1e1e1e;
    --grey:#6f6f6f;
    --mark-grey:#9a9a9a;
    --blue:#3276b5;
    --blue-bright:#0492cd;
    --pale-blue:#cee9f5;
    --pale-violet:#cfd3ec;
  }
  *{box-sizing:border-box;margin:0;padding:0}
  html,body{width:1200px;height:946px;overflow:hidden;background:var(--bg)}
  body{position:relative;font-family:"Questrial",sans-serif;color:var(--ink)}

  .card{
    position:absolute;width:620px;height:375px;background:var(--card);
    border-radius:26px;overflow:hidden;
  }
  .card--back{left:500px;top:70px}
  .card--front{left:80px;top:500px}

  /* back */
  .brand-stack{
    position:absolute;inset:0;display:flex;flex-direction:column;
    align-items:center;justify-content:center;gap:22px;
  }
  .brand-square{width:78px;height:78px;background:var(--mark-grey)}
  .brand-name{font-size:40px;letter-spacing:2px;color:var(--grey);text-transform:uppercase}

  /* front */
  .brand-row{position:absolute;left:36px;top:34px;display:flex;align-items:center;gap:14px}
  .brand-row .brand-square{width:44px;height:44px;background:var(--blue-bright)}
  .brand-row .brand-name{font-size:34px}

  .person{position:absolute;left:40px;top:150px}
  .person__name{font-size:20px;color:var(--blue);letter-spacing:1px;text-transform:uppercase;font-weight:700}
  .person__title{font-size:18px;margin-top:2px}

  .contacts{position:absolute;left:40px;top:222px;list-style:none;font-size:20px;line-height:30px}
  .contacts li{display:flex;align-items:center;gap:10px}
  .contacts svg{width:20px;height:20px;flex:none}
  .contacts .hl{color:var(--blue)}

  .backdrop{
    position:absolute;right:40px;top:96px;width:230px;height:250px;
    background:linear-gradient(135deg,var(--pale-violet),var(--pale-blue));opacity:.75;
  }
</style>
</head>
<body>

<section class="card card--back" aria-label="Card back">
  <div class="brand-stack">
    <span class="brand-square"></span>
    <span class="brand-name">Nimbra Tech</span>
  </div>
</section>

<section class="card card--front" aria-label="Card front">
  <div class="brand-row">
    <span class="brand-square"></span>
    <span class="brand-name">Nimbra Tech</span>
  </div>

  <div class="person">
    <p class="person__name">Rowan K. Hale</p>
    <p class="person__title">Managing Director</p>
  </div>

  <ul class="contacts">
    <li>
      <svg viewBox="0 0 20 20" aria-hidden="true"><path fill="#3276b5" d="M3 6c0-2 2-3 7-3s7 1 7 3v2h-4V6H7v2H3zM5 9h10l2 8H3z"/><circle cx="10" cy="13" r="2" fill="#fff"/></svg>
      <span>03 5550 0172</span>
    </li>
    <li>
      <svg viewBox="0 0 20 20" aria-hidden="true"><rect x="2" y="4" width="16" height="12" fill="#3276b5"/><path d="M2 4l8 7 8-7" fill="none" stroke="#fff" stroke-width="1.5"/></svg>
      <span>admin@nimbratech.com.au</span>
    </li>
    <li>
      <svg viewBox="0 0 20 20" aria-hidden="true"><circle cx="10" cy="10" r="8" fill="none" stroke="#3276b5" stroke-width="1.6"/><ellipse cx="10" cy="10" rx="3.5" ry="8" fill="none" stroke="#3276b5" stroke-width="1.2"/><path d="M2 10h16M4 6h12M4 14h12" stroke="#3276b5" stroke-width="1.2"/></svg>
      <span>www.<span class="hl">nimbratech</span>.com.au</span>
    </li>
  </ul>

  <div class="backdrop"></div>
</section>

</body>
</html>
```